Architectural, Engineering and Design Build

Tovantek4.com
Veteran Disabled Certified company is doing business in Architecture, Engineer and Design build - look simialr websites and come up with design follow following website
https://harlow-vessant.example/
https://www.quenforgroup.example/
https://www.ddelbmx.example/contract-vehicles/service-disabled-veteran-owned-small-business-sdvosb/
https://www.ostrelgrouplink.example/about/sdvosb/

Target Market(s)

US - Defense and Federal Government

Industry/Entity Type

Colors
0054AA
0677BA
7BADD7
CADEEF
E8F1F8

Requirements
Must have
• Army, American patriotism , Buildings, construction, architecture, engineering
Nice to have
• I need to attract federal government agencies and Defense

```html
<!DOCTYPE html>
<html lang="en">
<head>
<meta charset="utf-8">
<title>Architecture, Engineering &amp; Design Build</title>
<link href="https://fonts.googleapis.com/css2?family=Lato:wght@300;400;700;900&family=Ubuntu:wght@500;700&display=swap" rel="stylesheet">
<style>
:root{
  --navy:#1f2a63;
  --blue:#0054AA;
  --teal:#0677BA;
  --sky:#7BADD7;
  --pale:#CADEEF;
  --mist:#E8F1F8;
  --ink:#333;
  --text:#555;
  --muted:#8a8f98;
  --grey-bg:#f3f3f3;
  --footer:#2e3342;
  --footer-deep:#2a2e3b;
  --star:#f5c518;
  --quote:#a9c7dc;
  --white:#fff;
}
*{box-sizing:border-box;margin:0;padding:0}
html,body{width:1200px;height:3900px;overflow:hidden}
body{position:relative;font-family:"Lato",sans-serif;color:var(--ink);background:var(--white)}
.abs{position:absolute}
.center{text-align:center}

/* hero */
.hero{position:absolute;left:0;top:0;width:1200px;height:674px;overflow:hidden}
.hero-photo{position:absolute;inset:0;background:linear-gradient(100deg,#1c3a6e 0%,#2c4c7c 35%,#6f7b86 62%,#3a3f48 85%,#23272e 100%)}
.hero-shade{position:absolute;inset:0;background:linear-gradient(180deg,rgba(10,25,60,.45),rgba(10,20,40,.2) 60%,rgba(0,0,0,.35))}
.brand{position:absolute;left:125px;top:38px;font-family:"Ubuntu",sans-serif;font-weight:700;font-size:58px;letter-spacing:5px;color:var(--white)}
.nav{position:absolute;left:0;top:54px;width:1200px;font-family:"Ubuntu",sans-serif;font-weight:700;font-size:17px;color:var(--white)}
.nav a{position:absolute;color:inherit;text-decoration:none;white-space:nowrap}
.hero-title{position:absolute;left:0;width:1200px;top:296px;font-family:"Ubuntu",sans-serif;font-weight:700;font-size:36px;line-height:58px;color:var(--white);text-align:center}
.hero-btn{position:absolute;left:507px;top:438px;width:187px;height:51px;border:2px solid var(--white);border-radius:3px;color:var(--white);font-family:"Ubuntu",sans-serif;font-weight:700;font-size:16px;line-height:47px;text-align:center}

/* who we are */
.section-title{position:absolute;left:0;width:1200px;text-align:center;font-size:36px;font-weight:400;color:#3a3a3a}
.section-title b{font-weight:900}
.intro{position:absolute;left:0;width:1200px;top:816px;text-align:center;font-size:19px;line-height:36px;color:#444}
.service{position:absolute;top:967px;width:374px;height:346px;text-align:center}
.service.raised{background:var(--white);box-shadow:0 4px 22px rgba(0,0,0,.09)}
.service svg{position:absolute;left:145px;top:40px}
.service h3{position:absolute;left:0;width:100%;top:158px;font-size:23px;font-weight:700;color:#333}
.service p{position:absolute;left:50px;right:50px;top:200px;font-size:16px;line-height:27px;color:#444}

/* certification band */
.band{position:absolute;left:0;top:1427px;width:1200px;height:552px;background:var(--mist)}
.badge{position:absolute;left:155px;top:1548px}
.eyebrow{position:absolute;font-size:11px;font-weight:700;color:var(--teal);letter-spacing:.3px}
.heading-lg{position:absolute;font-size:37px;font-weight:300;line-height:48px;color:#333}
.copy{position:absolute;font-size:17px;line-height:30px;color:#444}
.subhead{position:absolute;font-size:22px;font-weight:400;color:#222}

/* stats */
.stats{position:absolute;left:642px;top:2068px;width:449px;height:279px;background:var(--white);box-shadow:0 6px 26px rgba(0,0,0,.08)}
.stat{position:absolute;width:224px;height:139px;text-align:center}
.stat strong{display:block;margin-top:36px;font-size:40px;font-weight:400;color:var(--navy)}
.stat span{display:block;margin-top:6px;font-size:14px;color:var(--muted)}
.stat span.small{font-size:12px}

/* testimonials */
.testimonials{position:absolute;left:8px;top:2505px;width:1192px;height:608px;background:var(--grey-bg)}
.world{position:absolute;left:160px;top:2570px;width:910px;height:480px;background:radial-gradient(ellipse at center,rgba(200,200,200,.45),rgba(243,243,243,0) 70%)}
.quote-card{position:absolute;top:2757px;width:464px;height:236px;background:var(--white);box-shadow:0 4px 16px rgba(0,0,0,.05)}
.avatar{position:absolute;left:30px;top:30px;width:94px;height:94px;border-radius:50%}
.quote-text{position:absolute;left:153px;top:36px;width:270px;font-size:13px;line-height:23px;color:#555}
.quote-name{position:absolute;left:153px;top:144px;font-size:17px;font-weight:700;color:#333}
.stars{position:absolute;left:153px;top:174px}
.quote-mark{position:absolute;right:32px;top:150px;font-family:"Ubuntu",sans-serif;font-weight:700;font-size:82px;line-height:82px;color:var(--quote)}
.round-btn{position:absolute;width:48px;height:48px;border-radius:50%;background:var(--white);box-shadow:0 2px 10px rgba(0,0,0,.08)}
.round-btn.outline{background:none;box-shadow:none;border:1.5px solid #333}
.round-btn svg{position:absolute;left:50%;top:50%;transform:translate(-50%,-50%)}

/* team */
.member{position:absolute;top:3238px;width:180px}
.member-photo{width:180px;height:182px}
.member-card{width:180px;height:85px;background:var(--white);box-shadow:0 4px 18px rgba(0,0,0,.08);text-align:center;padding-top:22px}
.member-card h4{font-size:18px;font-weight:400;color:#333}
.member-card p{margin-top:9px;font-size:11px;color:#666}

/* footer */
.footer{position:absolute;left:0;top:3605px;width:1200px;height:192px;background:var(--footer)}
.footer-logo{position:absolute;left:112px;top:3665px;font-family:"Ubuntu",sans-serif;font-weight:700;font-size:66px;letter-spacing:4px;color:#6a6e79}
.social{position:absolute;top:3677px;width:58px;height:58px;border-radius:50%;border:2px solid #bfc2c9}
.footer-bar{position:absolute;left:0;top:3797px;width:1200px;height:103px;background:var(--footer-deep);border-top:1px solid #8a8d96}
.footer-links{position:absolute;left:103px;top:3829px;font-size:15px;color:#c9ccd3;word-spacing:2px}
.footer-links i{font-style:normal;margin:0 14px;color:#9a9da5}
.copyright{position:absolute;right:72px;top:3829px;font-size:14px;color:#c9ccd3}
.dots{position:absolute;background-image:radial-gradient(#bbb 1.2px,transparent 1.3px);background-size:12px 12px}
</style>
</head>
<body>

<!-- HERO -->
<header class="hero">
  <div class="hero-photo" role="img" aria-label="Domed government capitol building with a national flag flying in front, under a deep blue sky"></div>
  <div class="hero-shade"></div>
  <div class="brand">LOGO</div>
  <nav class="nav">
    <a style="left:684px">ABOUT</a>
    <a style="left:780px">SERVICES</a>
    <a style="left:895px">PROJECTS</a>
    <a style="left:1015px">CONTACT</a>
  </nav>
  <h1 class="hero-title">Veteran Disabled Certified Company<br>Owned Business</h1>
  <div class="hero-btn">GET STARTED NOW</div>
</header>

<!-- WHO WE ARE -->
<h2 class="section-title" style="top:738px">Who <b>We Are</b></h2>
<p class="intro">Who We Are We only invest in post-product, post-revenue Enterprise IT startups. Usually, this means<br>you're at Seed Extension to Series A stage</p>

<div class="service" style="left:66px">
  <svg width="84" height="84" viewBox="0 0 84 84" fill="none" stroke="var(--teal)" stroke-width="3" stroke-linejoin="round">
    <path d="M6 10h56v52H6z"/><path d="M6 10c0-4 8-4 8 0v52"/><path d="M22 30h20M22 40h14"/>
    <path d="M48 74l30-30-8-8-30 30-2 10z"/><path d="M30 80h50L80 50z"/>
  </svg>
  <h3>Architecture</h3>
  <p>Lorem ipsum is simply dummy text printing typetting industry lorpsum has dummy uis aute.</p>
</div>
<div class="service raised" style="left:418px">
  <svg width="90" height="90" viewBox="0 0 90 90" fill="none" stroke="var(--teal)" stroke-width="3" stroke-linejoin="round">
    <rect x="4" y="24" width="56" height="56" rx="4"/>
    <circle cx="58" cy="24" r="10"/><path d="M58 8v6M58 34v6M42 24h6M68 24h6M47 13l4 4M65 31l4 4M47 35l4-4M65 17l4-4"/>
    <circle cx="28" cy="50" r="8"/><path d="M28 36v6M28 58v6M14 50h6M36 50h6"/>
    <path d="M46 60l26 26 6-6-26-26"/><path d="M12 70h20"/>
  </svg>
  <h3>Engineering</h3>
  <p>Lorem ipsum is simply dummy text printing typetting industry lorpsum has dummy uis aute.</p>
</div>
<div class="service" style="left:785px">
  <svg width="86" height="90" viewBox="0 0 86 90" fill="none" stroke="var(--teal)" stroke-width="3" stroke-linejoin="round">
    <rect x="4" y="14" width="78" height="56" rx="3"/><path d="M4 60h78M36 70l-4 12h22l-4-12M26 84h34"/>
    <path d="M46 44l24-28 6 5-24 28z"/><path d="M46 44c-6 0-10 4-10 8 6 0 10-2 10-8z"/><path d="M66 12l6-6 6 6-6 6"/>
  </svg>
  <h3>Design</h3>
  <p>Lorem ipsum is simply dummy text printing typetting industry lorpsum has dummy uis aute.</p>
</div>

<!-- CERTIFICATION -->
<section class="band"></section>
<svg class="badge" width="316" height="316" viewBox="0 0 316 316" role="img" aria-label="Certification seal">
  <circle cx="158" cy="158" r="150" fill="none" stroke="var(--blue)" stroke-width="16"/>
  <circle cx="158" cy="158" r="104" fill="none" stroke="#d0202a" stroke-width="3"/>
</svg>
<div class="eyebrow" style="left:552px;top:1516px">WHAT WE DO</div>
<h2 class="heading-lg" style="left:545px;top:1541px">Certification for Service Disabled<br>Veteran Owned Small Business</h2>
<p class="copy" style="left:549px;top:1657px">Lorem ipsum dolor amet consectetur adipiscing eiusmod temp<br>Lorem ipsum dolor sit amet consectetur adipiscing elit<br>do eiusmod tempor incididunt ut labore et dolore magna ut en<br>ad minim veniam nostrud exercitation.</p>
<h3 class="subhead" style="left:548px;top:1801px">Next Generation Enterprises</h3>
<p class="copy" style="left:549px;top:1841px">Lorem ipsum dolor amet consectetur adipiscing eiusmod temp<br>Lorem ipsum dolor sit amet consectetur</p>

<!-- STATS -->
<div class="eyebrow" style="left:116px;top:2070px">WHAT WE ACHIEVED</div>
<h2 class="heading-lg" style="left:112px;top:2093px">Proven Leadership.<br>Quality Engineering</h2>
<p class="copy" style="left:115px;top:2208px">We collect and analyze monthly purchase intent<br>data from a global network of IT decision<br>-makers.</p>
<p class="copy" style="left:115px;top:2310px">Lorem ipsum dolor amet consectetur adipiscing<br>Lorem ipsum dolor sit amet consectetur</p>

<svg class="abs" style="left:1000px;top:2050px" width="180" height="400" viewBox="0 0 180 400"><path d="M56 4L166 394 20 340z" fill="#eaf7ef"/></svg>
<div class="dots" style="left:600px;top:2250px;width:24px;height:130px"></div>
<div class="dots" style="left:600px;top:2348px;width:122px;height:36px"></div>
<div class="stats">
  <div class="stat" style="left:0;top:0;border-right:1px solid #eee;border-bottom:1px solid #eee"><strong>41</strong><span>Years in Business</span></div>
  <div class="stat" style="left:224px;top:0;border-bottom:1px solid #eee"><strong>97%</strong><span>Repeat Business</span></div>
  <div class="stat" style="left:0;top:139px;border-right:1px solid #eee"><strong>40%</strong><span>Professional Cerifications</span></div>
  <div class="stat" style="left:224px;top:139px"><strong>550+</strong><span class="small">Data Points</span></div>
</div>

<!-- TESTIMONIALS -->
<section class="testimonials"></section>
<div class="world" role="img" aria-label="Faint dotted world map"></div>
<div class="eyebrow center" style="left:0;width:1200px;top:2620px">TESTIMONIALS</div>
<h2 class="section-title" style="top:2643px">Words From <b>Clients</b></h2>

<div class="quote-card" style="left:127px">
  <div class="avatar" role="img" aria-label="Client portrait" style="background:radial-gradient(circle,#c9b8a4,#7d6a58)"></div>
  <p class="quote-text">when an unknown printer took a galley of type and scrambled it to make a type not only five centurie when an unknown printer took a galley of type</p>
  <div class="quote-name">Jon Castelvy</div>
  <svg class="stars" width="84" height="14" viewBox="0 0 84 14"><g fill="var(--star)"><path id="st" d="M7 0l2 5h5l-4 3 1.6 5L7 10l-4.6 3L4 8 0 5h5z"/><use href="#st" x="17"/><use href="#st" x="34"/><use href="#st" x="51"/></g><use href="#st" x="68" fill="#999"/></svg>
  <div class="quote-mark">”</div>
</div>
<div class="quote-card" style="left:627px">
  <div class="avatar" role="img" aria-label="Client portrait" style="background:radial-gradient(circle,#6e8aa0,#2f4a5e)"></div>
  <p class="quote-text">when an unknown printer took a galley of type and scrambled it to make a type not only five centurie when an unknown printer took a galley of type</p>
  <div class="quote-name">Kyle Fenwick</div>
  <svg class="stars" width="84" height="14" viewBox="0 0 84 14"><g fill="var(--star)"><use href="#st"/><use href="#st" x="17"/><use href="#st" x="34"/><use href="#st" x="51"/></g><use href="#st" x="68" fill="#999"/></svg>
  <div class="quote-mark">”</div>
</div>
<div class="round-btn" style="left:58px;top:2850px"><svg width="10" height="14" viewBox="0 0 10 14"><path d="M8 1L2 7l6 6" fill="none" stroke="#555" stroke-width="1.5"/></svg></div>
<div class="round-btn" style="left:1108px;top:2850px"><svg width="10" height="14" viewBox="0 0 10 14"><path d="M2 1l6 6-6 6" fill="none" stroke="#555" stroke-width="1.5"/></svg></div>

<!-- TEAM -->
<h2 class="section-title" style="top:3158px;left:24px">Meet Our <b>Team Members</b></h2>
<div class="round-btn outline" style="left:104px;top:3342px"><svg width="12" height="20" viewBox="0 0 12 20"><path d="M10 1L2 10l8 9" fill="none" stroke="#333" stroke-width="1.5"/></svg></div>
<div class="round-btn outline" style="left:1065px;top:3342px"><svg width="12" height="20" viewBox="0 0 12 20"><path d="M2 1l8 9-8 9" fill="none" stroke="#333" stroke-width="1.5"/></svg></div>
<div class="dots" style="left:164px;top:3455px;width:24px;height:92px"></div>
<div class="dots" style="left:164px;top:3520px;width:84px;height:28px"></div>

<div class="member" style="left:190px">
  <div class="member-photo" role="img" aria-label="Portrait of team member in a light blue shirt" style="background:linear-gradient(180deg,#fff 0%,#dfe5ee 40%,#7f98bf 100%)"></div>
  <div class="member-card"><h4>Rafiq D. Olsen</h4><p>Founder &amp; Managing Director</p></div>
</div>
<div class="member" style="left:415px">
  <div class="member-photo" role="img" aria-label="Portrait of team member in a dark shirt" style="background:linear-gradient(180deg,#fff 0%,#d9cfc6 40%,#2d3a4c 100%)"></div>
  <div class="member-card"><h4>Marc Halden</h4><p>Founder &amp; Ex CEO, Veristone</p></div>
</div>
<div class="member" style="left:643px">
  <div class="member-photo" role="img" aria-label="Portrait of team member in a plaid shirt" style="background:linear-gradient(180deg,#fff 0%,#d8c9bb 40%,#5c6b4e 100%)"></div>
  <div class="member-card"><h4>Arjun Vale</h4><p>Co-founder, Nuvanta (IPO),</p></div>
</div>
<div class="member" style="left:860px">
  <div class="member-photo" role="img" aria-label="Portrait of team member in a yellow top holding a cup" style="background:linear-gradient(180deg,#fff 0%,#e6d3c0 40%,#f0b728 100%)"></div>
  <div class="member-card"><h4>Tovin Sharo</h4><p>Co-founder, Dravio</p></div>
</div>

<!-- FOOTER -->
<footer class="footer"></footer>
<div class="footer-logo">LOGO</div>
<div class="social" style="left:744px" aria-label="Social link 1"></div>
<div class="social" style="left:821px" aria-label="Social link 2"></div>
<div class="social" style="left:900px" aria-label="Social link 3"></div>
<div class="social" style="left:977px" aria-label="Social link 4"></div>
<div class="social" style="left:1055px" aria-label="Social link 5"></div>
<div class="footer-bar"></div>
<div class="footer-links">Home<i>|</i>About<i>|</i>Services<i>|</i>Contact<i>|</i>About<i>|</i>Blog</div>
<div class="copyright">Copyright © 2024. All Rights Reserved.</div>

</body>
</html>
```